Business Card Design

Lintel Comms is a public relations consultancy service for the self build, home refurbishment and home improvement market.
It represents everything about 'home' so envisage logo featuring maybe roof pitch over the 'A' of Lintel. Colour/font undecided.

Industry/Entity Type

Home Improvement

Contact Information for Business Card

Fenella Coxworth
fenella@lintelcomms.co.uk
Telephone Direct: 0788 142 6597

```html
<!DOCTYPE html>
<html lang="en">
<head>
<meta charset="utf-8">
<title>Lintel Comms — Business Card</title>
<link rel="stylesheet" href="https://fonts.googleapis.com/css2?family=Oswald:wght@700&family=Michroma&display=swap">
<style>
  :root {
    --page-bg: #e9e7e3;
    --card-white: #ffffff;
    --ink-dark: #2b2b2b;
    --ink-mid: #4a4a4a;
    --swoosh-dark: #3a3a3a;
    --swoosh-light: #b9b9b9;
    --orange-light: #f7b21c;
    --orange-deep: #ee8a0c;
  }
  * { margin: 0; padding: 0; box-sizing: border-box; }
  html, body {
    width: 1200px; height: 800px; overflow: hidden;
    background: var(--page-bg);
  }
  .canvas {
    position: relative; width: 1200px; height: 800px;
    display: flex; align-items: center; justify-content: center;
  }
  .card {
    position: relative; width: 1050px; height: 600px;
    background: var(--card-white);
    box-shadow: 0 10px 30px rgba(0,0,0,0.18);
    overflow: hidden;
  }
  .card-art { position: absolute; inset: 0; }
  .identity {
    position: absolute; top: 62px; left: 220px; width: 470px;
    display: flex; flex-direction: column; align-items: center;
  }
  .brand {
    display: flex; align-items: center; gap: 18px;
  }
  .brand-square {
    width: 66px; height: 66px; background: var(--ink-dark);
  }
  .brand-name {
    font-family: 'Oswald', sans-serif; font-weight: 700;
    font-size: 58px; letter-spacing: 1px; line-height: 1;
    color: var(--ink-dark); white-space: nowrap;
  }
  .person {
    margin-top: 22px; text-align: center; color: var(--ink-mid);
    font-family: 'Michroma', sans-serif; white-space: nowrap;
  }
  .person-name { font-size: 20px; letter-spacing: 3px; }
  .person-title { font-size: 12px; letter-spacing: 3px; margin-top: 6px; }
  .contacts {
    position: absolute; right: 36px; bottom: 60px;
    font-family: 'Michroma', sans-serif; font-size: 15px;
    color: var(--ink-dark); text-align: right; letter-spacing: 1px;
  }
  .contact-line { display: flex; justify-content: flex-end; align-items: center; gap: 10px; margin-top: 10px; }
  .contact-item { display: inline-flex; align-items: center; gap: 6px; white-space: nowrap; }
  .icon { width: 16px; height: 16px; flex: none; }
</style>
</head>
<body>
<main class="canvas">
  <article class="card">
    <svg class="card-art" width="1050" height="600" viewBox="0 0 1050 600" aria-hidden="true">
      <defs>
        <linearGradient id="orangeFill" x1="0" y1="0" x2="1" y2="1">
          <stop offset="0" stop-color="#ee8a0c"/>
          <stop offset="0.5" stop-color="#f7b21c"/>
          <stop offset="1" stop-color="#ee8a0c"/>
        </linearGradient>
      </defs>
      <path class="swoosh-light" d="M0,298 Q600,438 1050,25 L1050,80 Q600,490 0,340 Z" fill="var(--swoosh-light)"/>
      <path class="swoosh-dark" d="M560,350 Q860,280 1050,28 L1050,75 Q880,320 560,350 Z" fill="var(--swoosh-dark)"/>
      <path class="orange-band" d="M0,335 Q600,480 1050,70 L1050,600 L0,600 Z" fill="url(#orangeFill)"/>
    </svg>

    <header class="identity">
      <div class="brand">
        <div class="brand-square"></div>
        <div class="brand-name">LINTEL COMMS</div>
      </div>
      <div class="person">
        <div class="person-name">FENELLA COXWORTH</div>
        <div class="person-title">FOUNDER</div>
      </div>
    </header>

    <div class="contacts">
      <div class="contact-line">
        <span class="contact-item">
          <svg class="icon" viewBox="0 0 16 16"><circle cx="8" cy="8" r="8" fill="var(--ink-dark)"/><path d="M8 3.5a3 3 0 0 0-3 3c0 2.2 3 6 3 6s3-3.8 3-6a3 3 0 0 0-3-3z" fill="#fff"/></svg>
          Unit 4, Ridge House, Bath BA1 2QT
        </span>
        <span class="contact-item">
          <svg class="icon" viewBox="0 0 16 16"><circle cx="8" cy="8" r="8" fill="var(--ink-dark)"/><circle cx="8" cy="8" r="4.5" fill="none" stroke="#fff" stroke-width="1.2"/><path d="M3.5 8h9M8 3.5v9" stroke="#fff" stroke-width="1"/></svg>
          www.lintelcomms.co.uk
        </span>
      </div>
      <div class="contact-line">
        <span class="contact-item">
          <svg class="icon" viewBox="0 0 16 16"><circle cx="8" cy="8" r="8" fill="var(--ink-dark)"/><path d="M5 4l2 2-1 1.5c.6 1.2 1.3 1.9 2.5 2.5L10 9l2 2-1.5 1.5C7 12 4 9 3.5 5.5z" fill="#fff"/></svg>
          0788 142 6597
        </span>
        <span class="contact-item">
          <svg class="icon" viewBox="0 0 16 16"><circle cx="8" cy="8" r="8" fill="var(--ink-dark)"/><rect x="5.5" y="3.5" width="5" height="9" rx="1" fill="#fff"/></svg>
          0788 531 2044
        </span>
        <span class="contact-item">
          <svg class="icon" viewBox="0 0 16 16"><circle cx="8" cy="8" r="8" fill="var(--ink-dark)"/><rect x="4" y="6" width="8" height="6" fill="#fff"/><rect x="5.5" y="3.5" width="5" height="3" fill="#fff"/></svg>
          0117 496 0382
        </span>
        <span class="contact-item">
          <svg class="icon" viewBox="0 0 16 16"><circle cx="8" cy="8" r="8" fill="var(--ink-dark)"/><rect x="3.5" y="5" width="9" height="6" fill="#fff"/><path d="M3.5 5L8 8.5 12.5 5" fill="none" stroke="var(--ink-dark)" stroke-width="1"/></svg>
          fenella@lintelcomms.co.uk
        </span>
      </div>
    </div>
  </article>
</main>
</body>
</html>
```